Two wall artworks for physiotherapy clinic waiting room

We are a physiotherapy clinic located in Glebe, Sydney. We have a clinic that is within a beautiful heritage listed building and we have two blank white walls that need artwork. Each artwork will be 3000mm wide and 1200mm high. Our clinic is mostly white and I will include our brand's colours below. We are looking for bright, beautiful artworks that are consistent with our colours. One of the artworks should include our full logo including the text so that customers see the name of the clinic on their way into the waiting room. I will include our logo in the files below, as well as images of the clinic, the walls and some other signs that we have already. We would prefer artworks with nice patterns or graphics rather than images of people.

```html
<!DOCTYPE html>
<html lang="en">
<head>
<meta charset="utf-8">
<title>Larkfield Physio – Waiting Room Wall Art</title>
<link rel="stylesheet" href="https://fonts.googleapis.com/css2?family=Montserrat:wght@500;600&family=Oswald:wght@600;700&display=swap">
<style>
  :root {
    --navy: #231a6b;
    --teal: #2fc3b9;
    --paper: #f4f3f8;
    --sky-top: #8fb6e2;
    --sky-low: #d3e3f2;
    --lavender: #b49ee0;
    --aqua: #2bb3d0;
    --shadow: #2b2546;
    --foliage: #5f8a62;
  }
  html, body { margin: 0; padding: 0; overflow: hidden; background: #ffffff; }
  .artwork {
    position: relative;
    width: 1200px;
    height: 488px;
    overflow: hidden;
    background: var(--paper);
    font-family: "Oswald", sans-serif;
  }
  .backdrop { position: absolute; inset: 0; }
  .brand {
    position: absolute;
    left: 58px;
    top: 100px;
    display: flex;
    align-items: center;
    gap: 18px;
  }
  .brand-dot {
    width: 58px; height: 58px; border-radius: 50%;
    background: var(--teal);
    flex: none;
  }
  .brand-text { display: flex; flex-direction: column; }
  .brand-name {
    font-family: "Montserrat", sans-serif;
    font-weight: 600;
    font-size: 46px;
    line-height: 1;
    color: var(--navy);
    letter-spacing: -0.5px;
  }
  .brand-tagline {
    margin-top: 8px;
    font-family: "Montserrat", sans-serif;
    font-weight: 500;
    font-size: 14px;
    color: var(--navy);
  }
  .headline {
    position: absolute;
    left: 57px;
    top: 187px;
    margin: 0;
    font-weight: 700;
    font-size: 31px;
    line-height: 36.5px;
    color: var(--navy);
    text-transform: uppercase;
  }
  .headline span { display: block; }
  .headline .accent { color: var(--teal); }
  .headline-rule {
    position: absolute; left: 57px; top: 303px;
    width: 44px; height: 2px; background: var(--teal);
  }
  .services {
    position: absolute;
    left: 57px;
    top: 347px;
    display: flex;
    gap: 17px;
    margin: 0; padding: 0; list-style: none;
  }
  .service {
    width: 100px;
    display: flex; flex-direction: column; align-items: center;
  }
  .service-icon {
    width: 70px; height: 60px;
    border: 1.5px solid var(--teal);
    display: flex; align-items: center; justify-content: center;
  }
  .service-label {
    margin-top: 8px;
    font-weight: 600;
    font-size: 16px;
    line-height: 18px;
    color: var(--navy);
    text-align: center;
    text-transform: uppercase;
    white-space: nowrap;
  }
  .service-rule { margin-top: 6px; width: 44px; height: 2px; background: var(--teal); }
</style>
</head>
<body>
<main class="artwork">
  <svg class="backdrop" width="1200" height="488" viewBox="0 0 1200 488">
    <defs>
      <linearGradient id="sky" x1="0" y1="0" x2="0" y2="1">
        <stop offset="0" stop-color="var(--sky-top)"/>
        <stop offset="0.55" stop-color="var(--sky-low)"/>
        <stop offset="1" stop-color="#a9c3dc"/>
      </linearGradient>
      <radialGradient id="glow-lavender" cx="0.5" cy="0.5" r="0.5">
        <stop offset="0" stop-color="var(--lavender)" stop-opacity="0.95"/>
        <stop offset="1" stop-color="var(--lavender)" stop-opacity="0"/>
      </radialGradient>
      <radialGradient id="glow-aqua" cx="0.5" cy="0.5" r="0.5">
        <stop offset="0" stop-color="var(--aqua)" stop-opacity="0.9"/>
        <stop offset="1" stop-color="var(--aqua)" stop-opacity="0"/>
      </radialGradient>
      <radialGradient id="glow-shadow" cx="0.5" cy="0.5" r="0.5">
        <stop offset="0" stop-color="var(--shadow)" stop-opacity="0.85"/>
        <stop offset="1" stop-color="var(--shadow)" stop-opacity="0"/>
      </radialGradient>
      <radialGradient id="glow-foliage" cx="0.5" cy="0.5" r="0.5">
        <stop offset="0" stop-color="var(--foliage)" stop-opacity="0.8"/>
        <stop offset="1" stop-color="var(--foliage)" stop-opacity="0"/>
      </radialGradient>
      <clipPath id="photo-clip">
        <polygon points="606,0 1200,0 1200,488 690,488 540,368 640,332 505,228 600,150"/>
      </clipPath>
    </defs>

    <g role="img" aria-label="Photo of two smiling cyclists in helmets riding bikes under a blue sky" clip-path="url(#photo-clip)">
      <rect x="500" y="0" width="700" height="488" fill="url(#sky)"/>
      <ellipse cx="570" cy="300" rx="130" ry="140" fill="url(#glow-foliage)"/>
      <ellipse cx="790" cy="240" rx="210" ry="190" fill="url(#glow-lavender)"/>
      <ellipse cx="950" cy="260" rx="150" ry="160" fill="url(#glow-aqua)"/>
      <ellipse cx="700" cy="400" rx="150" ry="110" fill="url(#glow-shadow)"/>
    </g>

    <!-- geometric accents -->
    <polygon points="334,0 504,0 504,79" fill="var(--teal)"/>
    <polygon points="505,85 602,143 505,194" fill="var(--navy)"/>
    <polygon points="498,219 632,297 495,358" fill="var(--teal)"/>
    <polygon points="0,200 55,244 0,298" fill="var(--teal)"/>
    <polygon points="1200,297 1200,452 1092,364" fill="var(--navy)"/>
    <g fill="var(--teal)">
      <polygon points="1020,410 1045,410 1075,445 1045,480 1020,480 1050,445"/>
      <polygon points="1060,410 1085,410 1115,445 1085,480 1060,480 1090,445"/>
      <polygon points="1100,400 1130,400 1200,460 1200,488 1170,488 1140,445"/>
    </g>
    <!-- plus marks -->
    <g stroke="var(--teal)" stroke-width="1.6">
      <path d="M53,36h9M57.5,31.5v9M68,36h9M72.5,31.5v9M53,50h9M57.5,45.5v9M68,50h9M72.5,45.5v9M53,64h9M57.5,59.5v9M68,64h9M72.5,59.5v9"/>
      <path d="M1152,345h9M1156.5,340.5v9M1167,345h9M1171.5,340.5v9M1152,359h9M1156.5,354.5v9M1167,359h9M1171.5,354.5v9M1152,373h9M1156.5,368.5v9M1167,373h9M1171.5,368.5v9"/>
    </g>
    <!-- dot grid -->
    <g fill="var(--teal)">
      <circle cx="383" cy="269" r="1.7"/><circle cx="396.5" cy="269" r="1.7"/><circle cx="410" cy="269" r="1.7"/><circle cx="423.5" cy="269" r="1.7"/><circle cx="437" cy="269" r="1.7"/><circle cx="450" cy="269" r="1.7"/>
      <circle cx="383" cy="283" r="1.7"/><circle cx="396.5" cy="283" r="1.7"/><circle cx="410" cy="283" r="1.7"/><circle cx="423.5" cy="283" r="1.7"/><circle cx="437" cy="283" r="1.7"/><circle cx="450" cy="283" r="1.7"/>
      <circle cx="383" cy="297" r="1.7"/><circle cx="396.5" cy="297" r="1.7"/><circle cx="410" cy="297" r="1.7"/><circle cx="423.5" cy="297" r="1.7"/><circle cx="437" cy="297" r="1.7"/><circle cx="450" cy="297" r="1.7"/>
      <circle cx="383" cy="310" r="1.7"/><circle cx="396.5" cy="310" r="1.7"/><circle cx="410" cy="310" r="1.7"/><circle cx="423.5" cy="310" r="1.7"/><circle cx="437" cy="310" r="1.7"/><circle cx="450" cy="310" r="1.7"/>
    </g>
  </svg>

  <div class="brand">
    <div class="brand-dot"></div>
    <div class="brand-text">
      <span class="brand-name">Larkfield Physio</span>
      <span class="brand-tagline">Physiotherapy and Exercise Physiology</span>
    </div>
  </div>

  <h1 class="headline">
    <span>Move better.</span>
    <span class="accent">Feel stronger.</span>
    <span>Live well.</span>
  </h1>
  <div class="headline-rule"></div>

  <ul class="services">
    <li class="service">
      <div class="service-icon">
        <svg width="48" height="48" viewBox="0 0 48 48">
          <rect x="14" y="6" width="10" height="6" rx="1.5" fill="var(--navy)"/>
          <rect x="14" y="14" width="10" height="6" rx="1.5" fill="var(--navy)"/>
          <rect x="14" y="22" width="10" height="6" rx="1.5" fill="var(--navy)"/>
          <path d="M4,34 q8,-4 16,0 h10 q3,0 3,3 h-12 M6,42 h20 l14,-8" stroke="var(--navy)" stroke-width="3" fill="none" stroke-linecap="round"/>
          <circle cx="34" cy="16" r="8" fill="var(--teal)"/>
          <path d="M34,12v8M30,16h8" stroke="#fff" stroke-width="2"/>
        </svg>
      </div>
      <span class="service-label">Physiotherapy</span>
      <span class="service-rule"></span>
    </li>
    <li class="service">
      <div class="service-icon">
        <svg width="48" height="48" viewBox="0 0 48 48">
          <circle cx="20" cy="7" r="4" fill="var(--navy)"/>
          <path d="M6,15 h30 M20,13 v16 M16,29 v14 M24,29 v14" stroke="var(--navy)" stroke-width="4" stroke-linecap="round"/>
          <path d="M28,27 h12 M29,23 v8 M39,23 v8" stroke="var(--teal)" stroke-width="3"/>
        </svg>
      </div>
      <span class="service-label">Exercise<br>Physiology</span>
      <span class="service-rule"></span>
    </li>
    <li class="service">
      <div class="service-icon">
        <svg width="48" height="48" viewBox="0 0 48 48">
          <rect x="14" y="4" width="18" height="11" rx="2" fill="var(--teal)"/>
          <circle cx="32" cy="26" r="4" fill="var(--navy)"/>
          <path d="M27,44 v-10 q5,-4 10,0 v10 z M28,32 l-6,-12" fill="var(--navy)" stroke="var(--navy)" stroke-width="3" stroke-linecap="round"/>
          <circle cx="8" cy="34" r="3" fill="var(--navy)"/><circle cx="17" cy="34" r="3" fill="var(--navy)"/>
          <path d="M3,44 q5,-8 10,0 z M12,44 q5,-8 10,0 z" fill="var(--navy)"/>
        </svg>
      </div>
      <span class="service-label">Movement<br>Classes</span>
      <span class="service-rule"></span>
    </li>
    <li class="service">
      <div class="service-icon">
        <svg width="48" height="48" viewBox="0 0 48 48">
          <path d="M24,3 l14,5 v10 q0,12 -14,18 q-14,-6 -14,-18 v-10 z" fill="var(--teal)"/>
          <path d="M24,8v10M19,13h10M18,23h12M18,28h10" stroke="#fff" stroke-width="2.2"/>
          <path d="M4,40 q8,-6 16,-2 h10 l10,-6 q3,0 2,3 l-12,9 h-26 z" fill="var(--navy)"/>
        </svg>
      </div>
      <span class="service-label">Injury<br>Prevention</span>
      <span class="service-rule"></span>
    </li>
  </ul>
</main>
</body>
</html>
```